Transfer Falcon - Cloud Based Data Migration Service for IT Professionals

We are looking for a smart clean website design for an informational site about our services and as a main portal into the service itself. We would like the design completed in WORDPRESS so that it will easily connect with the service.

Transfer Falcon is a cloud based migration service providing (to start with) a online migration tool that we migrate Quillnet Relay mailboxes (email) with all the settings, attachments from one system to another.
The service is aimed at IT professionals, IT companies and IT departments so our customers will be very technology based.

The Service -
IT companies currently migrate email; data and databases. using a very time intensive process which is both expensive and means their customer potentially losses access to its IT for a significant period of time. Additionally there are risks with regards to compatibility between systems and loss of data.
Potential benefits include;
• cost savings
• improved customer service, including reduced downtime
• improved resilience of the process
We are therefore developing cloud based migration software/website which will automate the process, mitigating these issues, as well as providing additional benefits such as the ability to sort and migrate only certain areas of data or certain emails, to check the integrity of the data/emails moved and to also repair corrupted data and emails.
The system will effectively duplicate the data and emails onto the new system over the weeks prior to the completion date. This will enable the IT Company to complete a final synchronisation and then immediately switch over to the new system with no interruption to the end users.
There is also an added benefit that the end users can test the system (with their own data and emails) prior to the switch over date to ensure everything is in place and databases work correctly.
The system will be completely cloud based and therefore easy for the IT Companies to access. They will be able to purchase the use of the system using CoinDrop or credit card and will only need to purchase what they need, this will allow even small local IT companies the facilities which previously would have been cost prohibitive to them.

Some of the sites we like for reference are -
Lanterbox, brightkits, the sky shifter.

We already have a logo design see attached and the website will need to work with this design.
Please message me if you have any questions
We do have the logo in other file formats if required.
Many Thanks

Target Market(s)

IT Sector

Industry/Entity Type

It Service

Number of Pages Required

5+ page

Requirements
Must have
• Front Page
• About Us
• Contact Info
• Blog
• Benefits
• More Information
• Must be Mobile Phone Compatible/friendly
• Log in (button) and support button on all pages (possibley top right)

```html
<!DOCTYPE html>
<html lang="en">
<head>
<meta charset="utf-8">
<title>Transfer Falcon – Cloud Data Migration</title>
<link rel="stylesheet" href="https://fonts.googleapis.com/css2?family=Montserrat:wght@300;400;600;700&family=Arimo:wght@400;700&display=swap">
<style>
  :root{
    --brand:#1aa3d9;
    --ink:#3a3a3a;
    --muted:#6b6b6b;
    --rule:#cfcfcf;
    --band:#2e7490;
    --footer:#1e1e1e;
    --footer-deep:#141414;
    --footer-text:#9a9a9a;
    --white:#ffffff;
    --head:'Montserrat', sans-serif;
    --body:'Arimo', sans-serif;
  }
  *{box-sizing:border-box;margin:0;padding:0}
  html,body{width:986px;height:1200px;overflow:hidden;background:var(--white)}
  body{position:relative;font-family:var(--body);color:var(--ink)}
  .abs{position:absolute}

  /* header */
  .site-header{position:absolute;left:0;top:0;width:986px;height:46px;background:var(--white)}
  .brand-name{position:absolute;left:210px;top:16px;font-family:var(--head);font-weight:600;font-size:11px;letter-spacing:1.2px;color:#222;text-transform:uppercase;display:flex;align-items:center;gap:6px}
  .brand-dot{width:12px;height:12px;border-radius:50%;background:var(--brand)}
  .main-nav a{position:absolute;top:20px;font-family:var(--head);font-size:6.5px;color:#444;text-decoration:none;letter-spacing:.3px}
  .main-nav a.active{color:var(--brand)}
  .nav-marker{position:absolute;left:569px;top:43px;width:22px;height:3px;background:var(--brand)}

  /* hero */
  .hero{position:absolute;left:0;top:46px;width:986px;height:252px;
    background:linear-gradient(100deg,#c9d3db 0%,#a9b8c4 35%,#7d8c98 60%,#3d434a 85%,#2b2f35 100%)}
  .hero-title{position:absolute;left:0;width:986px;top:96px;text-align:center;font-family:var(--head);font-weight:700;font-size:17.5px;line-height:23px;color:var(--white);text-shadow:0 1px 3px rgba(0,0,0,.55)}
  .hero-arrow{position:absolute;top:116px}

  /* migration intro */
  .intro-art{left:210px;top:344px;width:250px;height:128px;border-radius:6px;
    background:radial-gradient(circle at 45% 50%,#e3e6e9 0%,#eef1f3 45%,#ffffff 75%)}
  .section-title{font-family:var(--head);font-weight:400;color:var(--brand);text-transform:uppercase}
  .intro-title{left:500px;top:345px;font-size:17px}
  .short-rule{height:1px;width:24px;background:var(--rule)}
  .copy{font-size:7.4px;line-height:11.6px;color:var(--muted)}
  .btn-outline{left:500px;top:454px;width:76px;height:24px;border:1px solid #c4c4c4;border-radius:2px;font-family:var(--head);font-size:7.2px;color:#666;letter-spacing:.4px;display:flex;align-items:center;justify-content:center}
  .section-divider{left:0;top:503px;width:986px;height:1px;background:#e4e4e4}

  /* projects */
  .projects-title{left:210px;top:537px;font-size:16px;line-height:21px}
  .project-photo{top:540px;width:169px;height:98px}
  .photo-circuit{left:436px;background:radial-gradient(circle at 45% 55%,#ffd18a 0%,#e8782a 35%,#a8320e 75%,#6a1c08 100%)}
  .photo-building{left:621px;background:linear-gradient(160deg,#2b3138 0%,#8d99a3 40%,#d7dde2 55%,#56606a 80%,#1f2428 100%)}
  .caption{top:650px;font-family:var(--head);font-size:8.2px;color:#555}
  .read-more{font-family:var(--head);font-size:5.6px;font-weight:600;color:var(--brand);text-transform:uppercase;letter-spacing:.2px}

  /* strengths band */
  .strengths{left:0;top:736px;width:986px;height:236px;background:var(--band)}
  .strengths-title{left:0;width:986px;top:42px;text-align:center;font-family:var(--head);font-weight:300;font-size:18.5px;color:var(--white)}
  .strengths-title b{font-weight:700}
  .strength{top:84px;width:170px;text-align:center;color:var(--white)}
  .strength-icon{margin:0 auto;width:36px;height:36px}
  .icon-block{width:30px;height:34px;border-radius:4px;background:rgba(255,255,255,.85);margin:0 auto}
  .strength h3{margin-top:19px;font-family:var(--head);font-weight:600;font-size:8px;letter-spacing:.2px}
  .strength .bar{width:24px;height:1px;background:rgba(255,255,255,.7);margin:7px auto 8px}
  .strength p{font-size:6.8px;line-height:10.7px;padding:0 17px}

  /* footer */
  .site-footer{left:0;top:972px;width:986px;height:198px;background:var(--footer)}
  .footer-brand{left:210px;top:55px;font-family:var(--head);font-weight:600;font-size:12px;line-height:16px;color:var(--brand);letter-spacing:.8px;text-transform:uppercase;display:flex;align-items:center;gap:7px}
  .footer-brand span.dot{width:18px;height:18px;border-radius:50%;background:var(--brand);flex:none}
  .footer-head{top:52px;font-family:var(--head);font-weight:400;font-size:10.8px;color:#d0d0d0}
  .footer-rule{top:72px;width:24px;height:1px;background:#666}
  .footer-copy{left:351px;top:80px;width:160px;font-size:6.4px;line-height:11.4px;color:var(--footer-text)}
  .footer-contact{left:351px;top:121px;font-family:var(--head);font-size:8px;line-height:14.5px;color:#bdbdbd}
  .quick-links{left:568px;top:81px;list-style:none}
  .quick-links li{font-size:6.6px;color:var(--footer-text);height:17.6px}
  .social{left:705px;top:81px;width:100px;display:grid;grid-template-columns:1fr 1fr;row-gap:7px;column-gap:4px}
  .social span{display:flex;align-items:center;gap:3px;font-size:5.6px;color:var(--footer-text)}
  .social i{width:12px;height:12px;border:1.2px solid #8a8a8a;border-radius:50%;flex:none}
  .legal{left:0;top:1170px;width:986px;height:30px;background:var(--footer-deep);text-align:center;font-family:var(--head);font-size:7.2px;line-height:30px;color:#9a9a9a}
  .legal b{color:#e6e6e6;font-weight:400}
</style>
</head>
<body>

<header class="site-header">
  <div class="brand-name"><span class="brand-dot"></span>Transfer Falcon</div>
  <nav class="main-nav">
    <a class="active" style="left:569px">HOME</a>
    <a style="left:614px">ABOUT US</a>
    <a style="left:668px">BLOG</a>
    <a style="left:711px">BENIFITS</a>
    <a style="left:761px">CONTACT</a>
  </nav>
  <div class="nav-marker"></div>
</header>

<section class="hero" role="img" aria-label="Hand in a dark suit touching glowing cog wheels over a pale blue gear background">
  <h1 class="hero-title">CONSTANT DEVELOPMENT OF<br>CLOUD TECHNOLOGIES</h1>
  <svg class="hero-arrow" style="left:137px" width="12" height="22" viewBox="0 0 12 22"><path d="M11 1 1 11l10 10" fill="none" stroke="#fff" stroke-width="1.2"/></svg>
  <svg class="hero-arrow" style="left:851px" width="12" height="22" viewBox="0 0 12 22"><path d="M1 1l10 10L1 21" fill="none" stroke="#fff" stroke-width="1.2"/></svg>
</section>

<div class="abs intro-art" role="img" aria-label="Email envelopes flowing into a laptop inside a grey migration ring"></div>
<h2 class="abs section-title intro-title">Data and Email Migration</h2>
<div class="abs short-rule" style="left:500px;top:379px"></div>
<p class="abs copy" style="left:500px;top:389px;width:185px">Lorem ipsum dolor sit amet, consectetur adipiscing elit, sed do eiusmod tempor incididunt ut labore et dolore magna aliqua. Ut enim ad minim veniam, quis nostrud exercitation ullamco laboris nisi</p>
<div class="abs btn-outline">LEARN MORE</div>
<div class="abs section-divider"></div>

<h2 class="abs section-title projects-title">We<br>Accomplish Individual<br>Projects</h2>
<div class="abs short-rule" style="left:211px;top:615px"></div>
<p class="abs copy" style="left:210px;top:625px;width:185px">Lorem ipsum dolor sit amet, consectetur adipiscing elit, sed do eiusmod tempor incididunt ut labore et dolore magna aliqua. Ut enim ad minim veniam, quis nostrud exercitation ullamco laboris nisi</p>
<a class="abs read-more" style="left:211px;top:689px">Read more</a>

<div class="abs project-photo photo-circuit" role="img" aria-label="Close-up of a glowing orange circuit board"></div>
<div class="abs project-photo photo-building" role="img" aria-label="Curved glass and steel office atrium"></div>
<div class="abs caption" style="left:436px">Duis aute irure dolor in reprehenderit</div>
<div class="abs short-rule" style="left:436px;top:667px"></div>
<a class="abs read-more" style="left:436px;top:675px">Read more</a>
<div class="abs caption" style="left:621px">Duis aute irure dolor in reprehenderit</div>
<div class="abs short-rule" style="left:621px;top:667px"></div>
<a class="abs read-more" style="left:621px;top:675px">Read more</a>

<section class="abs strengths">
  <h2 class="abs strengths-title">Strength of Our <b>Business</b></h2>
  <div class="abs strength" style="left:218px">
    <div class="icon-block" role="img" aria-label="Engineer in a hard hat working at a laptop"></div>
    <h3>PROJECT RESEARCH</h3><div class="bar"></div>
    <p>Sed eleifend ornare metus, non rho ncus elit ultrices quis. Curabitur et met us ac sapien dictum</p>
  </div>
  <div class="abs strength" style="left:415px">
    <svg class="strength-icon" viewBox="0 0 40 36" aria-hidden="true">
      <ellipse cx="18" cy="14" rx="15" ry="9" fill="none" stroke="#fff" stroke-width="1.6"/>
      <path d="M10 21l-3 6 8-4" fill="none" stroke="#fff" stroke-width="1.6"/>
      <ellipse cx="27" cy="19" rx="10" ry="6" fill="#fff"/>
      <path d="M31 24l4 5-1-6z" fill="#fff"/>
    </svg>
    <h3>COMMUNITY SUPPORT</h3><div class="bar"></div>
    <p>Sed eleifend ornare metus, non rho ncus elit ultrices quis. Curabitur et met us ac sapien dictum</p>
  </div>
  <div class="abs strength" style="left:613px">
    <div class="icon-block" role="img" aria-label="Person beside a monitor showing gear settings"></div>
    <h3>INSPECTION &amp; TESTING</h3><div class="bar"></div>
    <p>Sed eleifend ornare metus, non rho ncus elit ultrices quis. Curabitur et met us ac sapien dictum</p>
  </div>
</section>

<footer class="abs site-footer">
  <div class="abs footer-brand"><span class="dot"></span>Transfer<br>Falcon</div>
  <h4 class="abs footer-head" style="left:352px">GET IN TOUCH WITH US</h4>
  <div class="abs footer-rule" style="left:352px"></div>
  <p class="abs footer-copy">Mes cuml dia sed in lacus ut eniascet ipsu ingerto aliiqt es site amet eismod ictor</p>
  <p class="abs footer-contact">TELEPHONE: +1 800 555 0142<br>E-MAIL: hello@transferfalcon.test</p>
  <h4 class="abs footer-head" style="left:567px">QUICK LINKS</h4>
  <div class="abs footer-rule" style="left:567px"></div>
  <ul class="abs quick-links">
    <li>Home</li><li>About Us</li><li>Blog</li><li>Benifits</li><li>Contact Us</li>
  </ul>
  <h4 class="abs footer-head" style="left:705px">SOCIAL LINKS</h4>
  <div class="abs footer-rule" style="left:705px"></div>
  <div class="abs social">
    <span><i></i>Chirpline</span>
    <span><i></i>Circlebook</span>
    <span><i></i>Pinboardly</span>
    <span><i></i>Linkwork</span>
  </div>
</footer>

<div class="abs legal"><b>Transfer Falcon</b> © 2016 Privacy policy</div>

</body>
</html>
```